whitening gel shopping website design

Hello:
We would like to create a whitening gel selling website. It will be very close to Glowbrite, but different designs. https://us.glowbriteorals.example/

What is your organization or website name?
Velvet Beaming

Industry: health and beauty
Target user: ladies between 16 to 40, please make the website friendly and lovely

website pages: main website, shop products, enrolled monthly plans, about us, contact us, policy, customer login log out, shopping cart, customer dashboard.

Website main page contains:
1. one slide show that shows advertisements.
2. show current promo codes
3.show a brief overview about our history
4. show a brief overview about the product introduction
5. show a brief overview of our monthly enrolled product plan
6. have an area to show blogs and posts (please take a look at Glowbrite home page)
7. buttons for customer to login, sign up, visit home, about us, policy, returns, subscription etc.

Note: for the contest, please finish the website main page and the product page only, now we don’t have any logo, test or images, please use yours for now.

```html
<!DOCTYPE html>
<html lang="en">
<head>
<meta charset="utf-8">
<title>Velvet Beaming — Teeth Whitening</title>
<link href="https://fonts.googleapis.com/css2?family=Roboto:ital,wght@0,400;0,500;0,700;1,400&family=Raleway:wght@300;400&display=swap" rel="stylesheet">
<style>
:root{
  --berry:#b3456f;
  --berry-deep:#8e2f58;
  --rose:#c4567c;
  --blush:#d7a0ad;
  --lavender:#d9d2ec;
  --lilac:#e9daf0;
  --ink:#1c1c1c;
  --muted:#6b6b6b;
  --night:#1a1a22;
  --navy:#1f2b48;
  --lime:#7cc35c;
  --sky:#3c8ad8;
  --sun:#f5c518;
  --red:#e11d48;
  --white:#ffffff;
}
*{box-sizing:border-box;margin:0;padding:0}
html,body{width:1200px;height:3982px;overflow:hidden}
body{position:relative;font-family:"Roboto",sans-serif;color:var(--ink);background:var(--white)}
.abs{position:absolute}
.heading{font-family:"Roboto",sans-serif;font-weight:700;font-size:29px;letter-spacing:.3px;color:var(--ink)}
.copy{font-family:"Raleway",sans-serif;font-weight:300;font-size:16.5px;line-height:24px;color:var(--muted);text-align:justify}
.outline-btn{border:2px solid var(--ink);background:var(--white);font-size:19px;display:flex;align-items:center;justify-content:center;color:var(--ink)}

/* top bar */
.topbar{left:0;top:0;width:1200px;height:27px;background:linear-gradient(90deg,#b84f7a,#a8426c);color:var(--white);font-size:12px}
.topbar .contact{left:34px;top:7px;display:flex;gap:30px;font-size:11px}
.topbar .account{right:22px;top:4px;display:flex;gap:12px;font-size:14px;align-items:center}
.dot{width:13px;height:13px;border-radius:50%;background:var(--white);display:inline-block}

/* nav */
.nav{left:0;top:27px;width:1200px;height:58px;background:var(--white);box-shadow:0 1px 3px rgba(0,0,0,.12)}
.brand{display:flex;align-items:center;gap:6px;font-family:"Roboto",sans-serif;font-weight:500;color:var(--ink)}
.nav .brand{left:62px;top:16px;font-size:15px}
.brand .mark{width:26px;height:26px;border-radius:50%;background:var(--ink)}
.menu{left:565px;top:22px;display:flex;gap:21px;font-size:16px}
.menu .active{position:relative}
.menu .active::after{content:"";position:absolute;left:0;right:0;bottom:-16px;height:2px;background:var(--rose)}
.cart{left:1030px;top:14px}

/* hero */
.hero{left:0;top:85px;width:1200px;height:400px;overflow:hidden}
.hero-photo{position:absolute;inset:0;background:linear-gradient(100deg,#c9a392 0%,#e8d2c6 30%,#f3e6e0 50%,#e2c2ae 75%,#c99d85 100%)}
.hero-title{left:104px;top:110px;width:420px;color:var(--white);font-size:31px;line-height:37px;font-weight:400;text-shadow:0 1px 3px rgba(0,0,0,.25)}
.hero-sub{left:106px;top:197px;width:460px;color:var(--white);font-size:10.5px;line-height:20px;font-weight:700}
.hero-btn{left:105px;top:265px;width:138px;height:36px;background:var(--rose);color:var(--white);font-size:19px;display:flex;align-items:center;justify-content:center}
.pager{left:575px;top:342px;display:flex;gap:14px}
.pager span{width:7px;height:7px;border-radius:50%;background:rgba(255,255,255,.8)}

/* history */
.history-bg{left:0;top:485px;width:1200px;height:481px;background:linear-gradient(180deg,#fafafa,#f3f3f3)}
.history-title{left:117px;top:556px}
.history-copy{left:116px;top:624px;width:522px}
.history-img{left:657px;top:549px;width:441px;height:348px;background:radial-gradient(ellipse at center,#4aa0e0 0%,#b9d9f2 45%,#f3f3f3 75%)}

/* offers */
.offers{left:0;top:966px;width:1200px;height:453px;background:linear-gradient(90deg,#c9cfe3,#dcd6ee 50%,#e2d4ef)}
.offers-title{left:0;width:1200px;top:20px;text-align:center;font-size:29px}
.offer{top:68px;width:274px;height:316px;background:linear-gradient(180deg,#e6e6e8,#f1f1f3)}
.offer .photo{position:absolute;inset:0;background:radial-gradient(ellipse at 50% 40%,#dde8f5,#e9e9ec 70%)}
.tag-new{left:0;top:0;background:var(--red);color:var(--white);font-size:15px;padding:2px 6px}
.offer .rating{left:0;width:100%;top:231px;text-align:center;color:#f3b21a;font-size:21px;letter-spacing:2px}
.offer .name{left:0;width:100%;top:256px;text-align:center;font-size:21px}
.offer .price{left:0;width:100%;top:283px;text-align:center;font-size:21px}
.discount{right:0;bottom:0;background:var(--red);color:var(--white);font-size:17px;padding:1px 6px}
.view{top:394px;width:100px;height:24px;background:var(--sun);color:#8a6d00;font-size:9px;display:flex;align-items:center;justify-content:center}

/* plans */
.plans-img{left:116px;top:1523px;width:356px;height:270px;background:linear-gradient(135deg,#f2f2f4,#dfe6ef 55%,#c4d8ef)}
.plans-title{left:499px;top:1504px}
.plans-copy{left:502px;top:1582px;width:580px}
.plans-btn{left:502px;top:1742px;width:115px;height:44px}

/* intro */
.intro{left:0;top:1894px;width:1200px;height:475px;background:linear-gradient(90deg,#cfcbe6,#e4d8ee 55%,#f2dcec)}
.intro-title{left:116px;top:78px}
.intro-copy{left:122px;top:154px;width:549px}
.intro-btn{left:117px;top:354px;width:115px;height:43px}
.intro-img{left:765px;top:54px;width:340px;height:355px;background:linear-gradient(160deg,#3b8fd9 0%,#bcdcf3 35%,#f4f4f6 70%)}

/* testimonials */
.testi{left:0;top:2369px;width:1200px;height:476px;background:linear-gradient(180deg,#c3778f,#d59ca8 60%,#d9a3ae)}
.testi-title{left:0;width:1200px;top:76px;text-align:center;color:var(--white);font-size:33px;font-weight:500}
.portrait{left:192px;top:135px}
.quote-mark{color:var(--white);font-family:"Roboto",sans-serif;font-weight:700;font-size:140px;line-height:1}
.testi-stars{left:518px;top:190px;color:var(--sun);font-size:19px;letter-spacing:3px}
.testi-text{left:515px;top:218px;width:430px;color:var(--white);font-style:italic;font-size:13.5px;line-height:18px}
.testi-name{left:514px;top:304px;color:var(--white);font-style:italic;font-weight:700;font-size:14px;line-height:18px}
.arrow{top:233px}

/* blogs */
.blogs-title{left:0;width:1200px;top:2900px;text-align:center;font-size:33px;font-weight:500}
.post{top:2968px;width:303px}
.post .photo{height:209px;background:linear-gradient(180deg,#f1dfd8,#e3c2b6 60%,#d9b3a5)}
.post .meta{margin-top:23px;display:flex;gap:4px;font-size:10px;color:var(--white)}
.meta .date{background:var(--lime);padding:2px 8px;color:#1e3a10}
.meta .count{background:var(--sky);padding:2px 6px}
.post h3{margin-top:12px;font-size:21px;font-weight:500;letter-spacing:.3px}
.post p{margin-top:8px;font-family:"Raleway",sans-serif;font-weight:300;font-size:16px;line-height:22px;color:var(--muted)}
.post .more{margin-top:14px;font-family:"Raleway",sans-serif;font-size:17px;color:#555}

/* footer */
.footer-shape{left:0;top:3480px}
.footer-brand{left:0;width:1200px;top:3588px;justify-content:center;color:var(--white);font-size:27px;font-weight:400}
.footer-brand .mark{width:44px;height:44px;background:var(--white)}
.social{left:127px;top:3638px;display:flex;gap:6px}
.social span{width:14px;height:14px;background:var(--white)}
.links{left:152px;top:3712px;list-style:none;color:var(--white);font-size:14.5px;line-height:22px}
.links li::before{content:"›";margin-right:12px;font-size:18px}
.register{left:470px;top:3712px;width:260px;text-align:center;color:var(--white);font-size:13px;line-height:18px}
.field{left:470px;width:260px;height:40px;border:1.5px solid var(--rose);color:var(--white);font-size:13px;display:flex;align-items:center;justify-content:center}
.contact-info{left:883px;top:3677px;color:#d9c4ca;font-size:14px;letter-spacing:.5px}
.info-row{left:885px;display:flex;gap:8px;align-items:center;color:var(--white);font-size:9px;line-height:11px}
.bottombar{left:0;top:3950px;width:1200px;height:32px;background:var(--navy);color:var(--white);font-size:12px;display:flex;align-items:center;justify-content:center}
</style>
</head>
<body>

<!-- top bar -->
<div class="abs topbar">
  <div class="abs contact"><span>☏ 888888888</span><span>info@Example.com</span></div>
  <div class="abs account"><span>Login</span><span>Sign up</span><span>Client Zone</span>
    <span class="dot"></span><span class="dot"></span><span class="dot"></span><span class="dot"></span></div>
</div>

<!-- navigation -->
<header class="abs nav">
  <div class="abs brand"><span class="mark"></span>Velvet Beaming</div>
  <nav class="abs menu"><span class="active">HOME</span><span>ABOUT US</span><span>PLANS</span><span>SHOP</span><span>CONTACT US</span></nav>
  <svg class="abs cart" width="36" height="32" viewBox="0 0 36 32">
    <path d="M2 6h5l4 15h15l4-11H9" fill="none" stroke="#1c1c1c" stroke-width="2.5"/>
    <circle cx="13" cy="26" r="2.5" fill="#1c1c1c"/><circle cx="24" cy="26" r="2.5" fill="#1c1c1c"/>
    <circle cx="30" cy="6" r="5" fill="#f3c3cf"/><text x="30" y="9" font-size="7" text-anchor="middle" fill="#b3456f">1</text>
  </svg>
</header>

<!-- hero slider -->
<section class="abs hero">
  <div class="hero-photo" role="img" aria-label="Smiling woman resting her head on her hands beside a blue teeth whitening light"></div>
  <h1 class="abs hero-title">LOREM IPSUM DOLOR SIT AMET, CONSECTETUR</h1>
  <p class="abs hero-sub">LOREM IPSUM DOLOR SIT AMET, CONSECTETUR ADIPISCING ELIT, SED DO EIUSMOD TEMPOR INCIDIDUNT UT LABORE ET DOLORE MAGNA ALIQUA. QUIS IPSUM SUSPENDISSE ULTRICES GRAVIDA.</p>
  <div class="abs hero-btn">Contact Us</div>
  <div class="abs pager"><span></span><span></span><span></span></div>
  <svg class="abs" style="left:0;top:0" width="1200" height="400" viewBox="0 0 1200 400">
    <defs><linearGradient id="heroWave" x1="0" x2="1"><stop offset="0" stop-color="#8e2f58"/><stop offset=".5" stop-color="#d06c8e"/><stop offset="1" stop-color="#9b3a62"/></linearGradient></defs>
    <path d="M0 370 C250 310 420 320 640 345 C860 370 1020 340 1200 300 L1200 400 L0 400Z" fill="url(#heroWave)"/>
    <path d="M0 400 L0 392 C260 350 430 352 650 372 C870 392 1030 365 1200 330 L1200 400Z" fill="#fafafa"/>
  </svg>
</section>

<!-- our history -->
<section class="abs history-bg"></section>
<h2 class="abs heading history-title">OUR HISTORY</h2>
<p class="abs copy history-copy">Lorem ipsum dolor sit amet, consectetur adipiscing elit, sed do eiusmod tempor incididunt ut labore et dolore magna aliqua. Quis ipsum suspendisse ultrices gravida. Risus commodo viverra maecenas accumsan lacus vel facilisis. Lorem ipsum dolor sit amet, consectetur adipiscing elit, sed do eiusmod tempor incididunt ut labore et dolore magna aliqua. Quis ipsum suspendisse ultrices gravida. Risus commodo viverra maecenas accumsan lacus vel facilisis.</p>
<div class="abs history-img" role="img" aria-label="Professional teeth whitening home kit box with blue light, gel syringe and mouth trays"></div>

<!-- special offers -->
<section class="abs offers">
  <h2 class="abs heading offers-title">SPECIAL OFFERS</h2>
  <div class="abs offer" style="left:187px">
    <div class="photo" role="img" aria-label="Whitening pen"></div>
    <span class="abs tag-new">New</span>
    <div class="abs rating">★★★★★</div>
    <div class="abs name">Lorem Ipsum</div>
    <div class="abs price">$00.00</div>
    <span class="abs discount">60% OFF</span>
  </div>
  <div class="abs offer" style="left:475px">
    <div class="photo" role="img" aria-label="Whitening toothpaste and gel tubes with brush heads"></div>
    <span class="abs discount">75% OFF</span>
  </div>
  <div class="abs offer" style="left:762px">
    <div class="photo" role="img" aria-label="Electric toothbrush with toothpaste tubes"></div>
    <span class="abs discount">33% OFF</span>
  </div>
  <div class="abs view" style="left:262px">click to view</div>
  <div class="abs view" style="left:562px">click to view</div>
  <div class="abs view" style="left:842px">click to view</div>
</section>

<!-- product plans -->
<div class="abs plans-img" role="img" aria-label="Whitening kit box with gel bottle and mouth tray"></div>
<h2 class="abs heading plans-title">PRODUCT PLANS</h2>
<p class="abs copy plans-copy">Lorem ipsum dolor sit amet, consectetur adipiscing elit, sed do eiusmod tempor incididunt ut labore et dolore magna aliqua. Quis ipsum suspendisse ultrices gravida. Risus commodo viverra maecenas accumsan lacus vel facilisis. Lorem ipsum dolor sit amet, consectetur adipiscing elit, sed do eiusmod tempor incididunt ut labore et dolore</p>
<div class="abs outline-btn plans-btn">Read More</div>

<!-- product introduction -->
<section class="abs intro">
  <h2 class="abs heading intro-title">PRODUCT INTRODUCTION</h2>
  <p class="abs copy intro-copy">Lorem ipsum dolor sit amet, consectetur adipiscing elit, sed do eiusmod tempor incididunt ut labore et dolore magna aliqua. Quis ipsum suspendisse ultrices gravida. Risus commodo viverra maecenas accumsan lacus vel facilisis.Lorem ipsum dolor sit amet, consectetur adipiscing elit, sed do eiusmod tempor incididunt ut labore et dolore magna aliqua. Quis ipsum suspendisse ultrices gravida. Risus commodo viverra maecenas accumsan lacus vel facilisis.</p>
  <div class="abs outline-btn intro-btn">Learn More</div>
  <div class="abs intro-img" role="img" aria-label="Advanced teeth whitening kit box with gel pens and light tray"></div>
</section>

<!-- testimonials -->
<section class="abs testi">
  <h2 class="abs testi-title">OUR TESTIMONIALS</h2>
  <svg class="abs portrait" width="186" height="163" viewBox="0 0 186 163">
    <polygon points="46,3 140,3 183,81 140,160 46,160 3,81" fill="#e8e4e2" stroke="#ffffff" stroke-width="5"/>
    <polygon points="52,12 134,12 172,81 134,151 52,151 14,81" fill="#b9b2ad" role="img" aria-label="Portrait of the customer"/>
  </svg>
  <div class="abs quote-mark" style="left:410px;top:120px">“</div>
  <div class="abs testi-stars">★★★★</div>
  <p class="abs testi-text">Lorem ipsum dolor sit amet, consectetur adipiscing elit, sed do eiusmod tempor incididunt ut labore et dolore magna aliqua. Quis ipsum suspendisse ultrices gravida. Risus commodo viverra maecenas accumsan lacus vel facilisis.</p>
  <p class="abs testi-name">- Daniel Harlow.<br>Creative Manager,USA</p>
  <div class="abs quote-mark" style="left:800px;top:286px">”</div>
  <svg class="abs arrow" style="left:116px" width="30" height="34" viewBox="0 0 30 34"><path d="M24 3 L8 17 L24 31" fill="none" stroke="#fff" stroke-width="6"/></svg>
  <svg class="abs arrow" style="left:1052px" width="30" height="34" viewBox="0 0 30 34"><path d="M6 3 L22 17 L6 31" fill="none" stroke="#fff" stroke-width="6"/></svg>
</section>

<!-- latest blogs -->
<h2 class="abs blogs-title">OUR LATEST BLOGS</h2>
<article class="abs post" style="left:116px">
  <div class="photo" role="img" aria-label="Close-up of a bright white smile"></div>
  <div class="meta"><span class="date">8-MAR-19</span><span class="count">💬 08</span></div>
  <h3>LOREM IPSUM DOLOR SIT</h3>
  <p>Lorem ipsum dolor sit amet, consectetur adipiscing elit, sed do eiusmod tempor incididunt ut labore et dolore magna aliqua.</p>
  <div class="more">Read more..</div>
</article>
<article class="abs post" style="left:445px">
  <div class="photo" role="img" aria-label="Close-up of a whitening light tray held in the mouth"></div>
  <div class="meta"><span class="date">8-MAR-19</span><span class="count">💬 08</span></div>
  <h3>LOREM IPSUM DOLOR SIT</h3>
  <p style="margin-top:2px">Lorem ipsum dolor sit amet, consectetur adipiscing elit, sed do eiusmod tempor incididunt ut labore et dolore magna aliqua.</p>
  <div class="more">Read more..</div>
</article>
<article class="abs post" style="left:776px">
  <div class="photo" role="img" aria-label="Close-up of a bright white smile"></div>
  <div class="meta"><span class="date">8-MAR-19</span><span class="count">💬 08</span></div>
  <h3>LOREM IPSUM DOLOR SIT</h3>
  <p>Lorem ipsum dolor sit amet, consectetur adipiscing elit, sed do eiusmod tempor incididunt ut labore et dolore magna aliqua.</p>
  <div class="more">Read more..</div>
</article>

<!-- footer -->
<svg class="abs footer-shape" width="1200" height="470" viewBox="0 0 1200 470">
  <defs><linearGradient id="footArc" x1="0" x2="1"><stop offset="0" stop-color="#8e2f58"/><stop offset=".5" stop-color="#d0708f"/><stop offset="1" stop-color="#a03e66"/></linearGradient></defs>
  <path d="M40 150 C300 20 900 20 1180 130 L1200 140 L1200 470 L0 470 L0 170Z" fill="url(#footArc)"/>
  <path d="M0 180 C300 45 900 45 1200 160 L1200 470 L0 470Z" fill="#1a1a22"/>
</svg>
<div class="abs brand footer-brand"><span class="mark"></span>Velvet Beaming</div>
<div class="abs social"><span></span><span></span><span></span><span></span></div>
<ul class="abs links">
  <li>HOME</li><li>ABOUT US</li><li>PLANS</li><li>SHOP</li><li>CONTACT US</li><li>PRIVACY POLICY</li><li>RETURNS</li><li>SUBSCRIPTION</li>
</ul>
<p class="abs register">Register your Email Address to get<br>more Information about us</p>
<div class="abs field" style="top:3791px">Email Address*</div>
<div class="abs field" style="top:3840px">SUBSCRIBE</div>
<div class="abs contact-info">CONTACT INFORMATION</div>
<div class="abs info-row" style="top:3732px"><svg width="12" height="12" viewBox="0 0 12 12"><path d="M2 1h3l1 3-2 1c1 2 2 3 4 4l1-2 3 1v3C5 11 1 7 2 1z" fill="#fff"/></svg>1234567891</div>
<div class="abs info-row" style="top:3760px"><svg width="12" height="14" viewBox="0 0 12 14"><circle cx="6" cy="4" r="3" fill="#fff"/><path d="M0 14c0-4 3-6 6-6s6 2 6 6z" fill="#fff"/></svg>Risus commodo viverra maecenas<br>viverra maecenas</div>
<div class="abs info-row" style="top:3794px"><svg width="14" height="10" viewBox="0 0 14 10"><rect x=".5" y=".5" width="13" height="9" fill="none" stroke="#fff"/><path d="M.5 .5 7 6 13.5 .5" fill="none" stroke="#fff"/></svg>info@example.com</div>
<div class="abs bottombar">copyright © 2019 velvetbeaming.example | All Rights Reserved</div>

</body>
</html>
```